Peter Lundell Sausage Label Design

Halden Acres Corporation is seeking to create a new brand of fresh 100% Canadian pork sausage. This label will be a paper band that slips on and off foam trays. The front facing side will be 5 inches wide by 3.5 inches high. The following is some information about our brand.
Target market:
1. Working Moms
2. Stay at home moms
3. Barbeque enthusiast
Brand personality
1. Old school values – We are a family run company who believes in an honest days work
2. Modern day sensibility – We believe in being nimble and open to new ideas
3. Energetic and optimistic – We are passionate about our business and product
4. Relaxed sense of humor – We believe that it is possible to work hard and have fun
Positioning Statements:
Our sausage is the easy choice for adding flavour to your real- life family meals, that’s because:
1. It is 100% fresh Canadian product with no fillers or preservatives
2. It is a great tasting recipe with simple, natural ingredients
3. It is brought to you with good humor and integrity by a multi- generational family owned business
We are looking for a creative designer to make our ideas come to life. There are three types of designs we would like to see:
1. Rustic – a rustic, barbequing, old farm, country feel – without feeling too old
2. Modern & Simple – Very simple clean face with clean text
3. Family friendly – a label that would appeal to the everyday family with photos of the finished product
This brand does not have a name yet, please use the name “Peter Lundell “as a place holder. Please keep in mind the information provided about our brand when developing the label. Attached are pictures of some ideas we like. Please do not copy these ideas too closely, we are looking to differentiate ourselves in the market. Samples are to provide some guidance of our preferences.
Updates
Target Market(s)
1. Working Moms
2. Stay at home moms
3. Barbeque enthusiast
Colors
Designer to choose colors to be used in the design.
Look and feel
Each slider illustrates characteristics of the customer's brand and the style your logo design should communicate.

```html
<!DOCTYPE html>
<html lang="en">
<head>
<meta charset="utf-8">
<title>Peter Lundell – Smoked Pork Sausage Label</title>
<link rel="stylesheet" href="https://fonts.googleapis.com/css2?family=Montserrat:wght@500;600;700&family=Pinyon+Script&display=swap">
<style>
  :root {
    --navy: #1d2a49;
    --gold: #c6943f;
    --gold-soft: #d8b06a;
    --paper: #ebe3d5;
    --paper-edge: #e2d8c6;
    --ink-grey: #4b4e57;
    --page: #ffffff;
  }
  * { box-sizing: border-box; margin: 0; padding: 0; }
  html, body {
    width: 1200px; height: 702px; overflow: hidden;
    background: var(--page);
    font-family: "Montserrat", Arial, sans-serif;
  }
  .label {
    position: absolute; left: 170px; top: 51px;
    width: 860px; height: 600px;
    background: radial-gradient(ellipse at 40% 35%, #efe8db 0%, var(--paper) 60%, var(--paper-edge) 100%);
    color: var(--navy);
  }
  .frame-line { position: absolute; background: var(--navy); }
  .frame-line--top { left: 8px; right: 8px; top: 18px; height: 1.5px; }
  .frame-line--bottom { left: 8px; right: 8px; bottom: 18px; height: 1.5px; }
  .frame-line--left { top: 8px; bottom: 8px; left: 16px; width: 1.5px; }
  .frame-line--right { top: 8px; bottom: 8px; right: 16px; width: 1.5px; }

  .brand {
    position: absolute; left: 92px; top: 51px;
    width: 216px; height: 216px;
    display: flex; align-items: center; justify-content: center;
  }
  .brand__ring {
    position: absolute; inset: 0;
    border: 3px solid var(--navy); border-radius: 50%;
  }
  .brand__name {
    position: relative;
    font-family: "Montserrat", Arial, sans-serif;
    font-weight: 700; font-size: 29px; line-height: 1.1;
    text-align: center; color: var(--navy); letter-spacing: 0.5px;
  }

  .pig-illustration {
    position: absolute; left: 357px; top: 77px;
    width: 452px; height: 212px;
    background: radial-gradient(ellipse at 50% 50%, var(--gold-soft) 0%, var(--gold) 55%, rgba(198,148,63,0) 72%);
    opacity: 0.85;
  }

  .title-band {
    position: absolute; left: 49px; top: 295px;
    width: 756px; height: 84px;
    background: var(--navy);
    display: flex; align-items: center; justify-content: center;
  }
  .title-band::after {
    content: ""; position: absolute; inset: 5px;
    border: 1.5px solid var(--gold);
  }
  .title-band__text {
    color: #fff; font-weight: 500; font-size: 39px; letter-spacing: 3px;
  }

  .tagline {
    position: absolute; left: 0; right: 0; top: 398px;
    display: flex; align-items: center; justify-content: center; gap: 16px;
    font-family: "Pinyon Script", cursive;
    font-size: 38px; color: var(--navy);
  }
  .tagline__dash { width: 26px; height: 1.5px; background: var(--gold); }

  .facts {
    position: absolute; left: 49px; top: 471px;
    width: 756px; height: 110px;
    border-top: 1.5px solid var(--navy);
    border-bottom: 1.5px solid var(--navy);
  }
  .facts__origin {
    position: absolute; left: 0; top: 0; width: 231px; height: 100%;
    border-right: 1.5px solid var(--navy);
  }
  .origin__map {
    position: absolute; left: 102px; top: 16px; width: 112px; height: 78px;
    background: radial-gradient(ellipse at 50% 55%, var(--gold) 0%, var(--gold) 50%, rgba(198,148,63,0) 72%);
  }
  .origin__text {
    position: relative; padding-top: 43px;
    font-weight: 600; color: var(--navy); line-height: 1.15;
  }
  .origin__pct { display: block; font-size: 26px; letter-spacing: 1px; }
  .origin__kind { display: block; font-size: 19px; letter-spacing: 1px; }

  .facts__cells {
    position: absolute; left: 231px; top: 0; right: 0; height: 68px;
    display: flex;
    border-bottom: 1.5px dotted var(--navy);
  }
  .fact {
    padding: 10px 0 0 10px; border-right: 1.5px solid var(--navy);
  }
  .fact:last-child { border-right: none; }
  .fact--grazing { width: 184px; }
  .fact--pieces { width: 146px; }
  .fact--weight { flex: 1; }
  .fact__label { display: block; font-weight: 600; font-size: 18px; letter-spacing: 1.5px; }
  .fact__value { display: block; font-weight: 500; font-size: 20px; color: var(--ink-grey); letter-spacing: 1px; }
  .fact--weight .fact__value {
    color: var(--gold); font-weight: 600; font-size: 27px; letter-spacing: 2px;
    padding-left: 44px; line-height: 1;
  }
  .facts__web {
    position: absolute; left: 231px; right: 0; top: 79px;
    text-align: center; color: var(--gold);
    font-weight: 600; font-size: 20px; letter-spacing: 3.5px;
  }
</style>
</head>
<body>
  <section class="label" aria-label="Smoked pork sausage label">
    <span class="frame-line frame-line--top"></span>
    <span class="frame-line frame-line--bottom"></span>
    <span class="frame-line frame-line--left"></span>
    <span class="frame-line frame-line--right"></span>

    <div class="brand">
      <span class="brand__ring"></span>
      <span class="brand__name">Peter<br>Lundell</span>
    </div>

    <div class="pig-illustration" role="img" aria-label="Engraved-style gold illustration of a pig standing in profile"></div>

    <div class="title-band">
      <h1 class="title-band__text">SMOKED PORK SAUSAGE</h1>
    </div>

    <p class="tagline">
      <span class="tagline__dash"></span>
      <span>Exquisitely tender, and succulent taste</span>
      <span class="tagline__dash"></span>
    </p>

    <div class="facts">
      <div class="facts__origin">
        <div class="origin__map" role="img" aria-label="Gold map of Canada"></div>
        <p class="origin__text">
          <span class="origin__pct">100%</span>
          <span class="origin__kind">CANADIAN PORK</span>
        </p>
      </div>
      <div class="facts__cells">
        <div class="fact fact--grazing">
          <span class="fact__label">GRAZING:</span>
          <span class="fact__value">Grass - fed</span>
        </div>
        <div class="fact fact--pieces">
          <span class="fact__label">PIECES:</span>
          <span class="fact__value">6 sausages</span>
        </div>
        <div class="fact fact--weight">
          <span class="fact__label">NET WT.:</span>
          <span class="fact__value">500G</span>
        </div>
      </div>
      <p class="facts__web">WWW.PETER-LUNDELL.COM</p>
    </div>
  </section>
</body>
</html>
```